A website for Veltranor Limited

We need a new and modern website for our company. We are engineering consultants and contractors (EPC) in the oil and gas industry and building services industry.
What we do:
Engineering, procurement, construction
Automation (safety and process)
Non-destructive testing
Training
We have an existing website and the content can be referred from there since we are remaking the website
For more information visit Veltranor Limited Kenya

```html
<!DOCTYPE html>
<html lang="en">
<head>
<meta charset="utf-8">
<title>Veltranor Limited</title>
<link href="https://fonts.googleapis.com/css2?family=Poppins:wght@400;500;600;700;800&display=swap" rel="stylesheet">
<style>
:root{
  --orange:#e8733a;
  --orange-light:#f4b35f;
  --grad:linear-gradient(90deg,#e8733a,#f4b35f);
  --ink:#1f1f1f;
  --text:#444;
  --muted:#8a8a8a;
  --dark:#2b2b2d;
  --white:#fff;
}
*{margin:0;padding:0;box-sizing:border-box}
html,body{width:1200px;height:3911px;overflow:hidden}
body{font-family:'Poppins',sans-serif;color:var(--text);background:var(--white);position:relative}
.abs{position:absolute}
.slant{clip-path:polygon(14% 0,100% 0,86% 100%,0 100%)}

/* header */
.topbar{left:680px;top:0;width:520px;height:38px;background:var(--grad);clip-path:polygon(4% 0,100% 0,100% 100%,0 100%);display:flex;justify-content:flex-end;align-items:center;gap:22px;padding-right:88px;font-size:15px;color:var(--white)}
.brand{left:87px;top:8px;display:flex;align-items:center;gap:8px}
.brand-mark{width:76px;height:76px;border-radius:50%;border:3px solid var(--orange)}
.brand-name{font-size:21px;line-height:30px;color:var(--muted);font-weight:400;letter-spacing:.5px}
.nav{left:518px;top:64px;display:flex;align-items:center;gap:28px;font-size:14px;font-weight:500;color:#555;letter-spacing:.3px}

/* hero */
.hero{left:0;top:106px;width:1200px;height:718px;background:linear-gradient(120deg,#2e3236 0%,#4a4f55 45%,#6b6f73 70%,#3a3d40 100%)}
.hero-accent{left:660px;top:200px;width:480px;height:530px;background:linear-gradient(160deg,rgba(244,179,95,.75),rgba(232,115,58,.75));clip-path:polygon(40% 0,100% 0,60% 100%,0 100%)}
.hero h1{left:86px;top:328px;font-size:52px;line-height:58px;font-weight:700;color:var(--white);width:600px}
.hero-sub{left:86px;top:516px;font-size:16px;color:var(--white)}
.btn-orange{background:var(--grad);color:var(--white);font-size:14px;font-weight:700;display:flex;align-items:center;justify-content:center;letter-spacing:.4px}
.arrow{width:58px;height:50px;background:var(--white);display:flex;align-items:center;justify-content:center}

/* section titles */
.title{font-size:46px;font-weight:700;color:var(--ink);letter-spacing:-.5px}

/* who */
.who-frame{left:112px;top:917px;width:440px;height:450px;background:linear-gradient(200deg,#f4b35f,#e8733a);clip-path:polygon(22% 0,100% 0,78% 100%,0 100%)}
.who-photo{left:187px;top:962px;width:318px;height:358px;background:linear-gradient(180deg,#6f9fd0 0%,#a8c6e4 45%,#7a7a78 75%,#5a5550 100%);box-shadow:0 30px 40px rgba(0,0,0,.18)}
.who-text{left:588px;top:1084px;width:500px;font-size:15px;line-height:26px}
.btn-outline{border:2px solid var(--orange);color:var(--ink);font-size:14px;font-weight:700;display:flex;align-items:center;justify-content:center;clip-path:polygon(0 0,100% 0,88% 100%,0 100%)}

/* cards */
.card{top:1525px;width:244px;height:283px;background:var(--white);box-shadow:0 8px 24px rgba(0,0,0,.12)}
.card-img{width:244px;height:196px}
.card-icon{position:absolute;left:40px;top:152px;width:74px;height:58px;background:var(--grad);clip-path:polygon(30% 0,100% 0,70% 100%,0 100%)}
.card-label{position:absolute;left:21px;top:222px;font-size:14px;line-height:17px;font-weight:700;color:var(--ink);width:210px}

/* projects */
.proj{top:1990px;width:400px;height:440px}
.proj-overlay{left:415px;top:2005px;width:375px;height:410px;background:linear-gradient(180deg,rgba(232,115,58,.92),rgba(244,179,95,.88))}
.round-btn{width:44px;height:40px;background:var(--white);display:flex;align-items:center;justify-content:center;clip-path:polygon(20% 0,100% 0,80% 100%,0 100%)}

/* review */
.review-text{left:128px;top:2683px;width:552px;font-size:15px;line-height:26px}
.review-name{left:128px;top:2820px;font-size:14px;font-weight:700;color:var(--orange)}
.collage{left:645px;top:2555px;width:438px;height:455px;background:#ececec;clip-path:polygon(40% 0,100% 0,60% 100%,0 100%)}
.tile{clip-path:polygon(30% 0,100% 0,70% 100%,0 100%)}

/* partners */
.partners{left:0;top:3100px;width:1200px;display:flex;justify-content:center;align-items:center;gap:44px}
.partner{display:flex;align-items:center;gap:8px;font-size:18px;font-weight:600;color:#8c8c8c}
.partner i{width:26px;height:26px;border-radius:50%;background:#c9c9c9;display:block}

/* footer */
.footer{left:0;top:3415px;width:1200px;height:496px;background:var(--dark)}
.cta{left:178px;top:3300px;width:847px;height:172px;background:linear-gradient(90deg,#e8733a,#f0a055 60%,#f4b35f);clip-path:polygon(12% 0,100% 0,88% 100%,0 100%)}
.cta h2{left:370px;top:3350px;font-size:38px;line-height:42px;color:var(--white);font-weight:700}
.foot-col{top:3592px;font-size:12px;line-height:19px;color:#d0d0d0}
.foot-col b{color:var(--white);font-weight:600;display:block}
.ico{color:var(--orange);margin-right:4px}
.copy{left:0;top:3870px;width:1200px;text-align:center;font-size:14px;color:var(--white)}
</style>
</head>
<body>

<!-- header -->
<div class="abs topbar"><span>Our Clients</span><span>Where we Operate</span><span>Our Partners</span></div>
<div class="abs brand"><span class="brand-mark"></span><span class="brand-name">VELTRANOR<br>LIMITED</span></div>
<nav class="abs nav">
  <svg width="16" height="14" viewBox="0 0 16 14"><path d="M8 0 16 7h-2.5v7h-4V9.5h-3V14h-4V7H0z" fill="#e8733a"/></svg>
  <span>ABOUT US</span><span>SERVICES</span><span>PRODUCTS</span><span>PROJECTS</span><span>CONTACTS</span>
  <svg width="20" height="24" viewBox="0 0 20 24"><rect x="1" y="6" width="18" height="17" fill="none" stroke="#999" stroke-width="1.5"/><path d="M6 9V5a4 4 0 0 1 8 0v4" fill="none" stroke="#999" stroke-width="1.5"/></svg>
</nav>

<!-- hero -->
<section class="abs hero" role="img" aria-label="Photo of two engineers in hard hats reviewing plans"></section>
<div class="abs hero-accent"></div>
<h1 class="abs hero h1" style="left:86px;top:328px;font-size:52px;line-height:58px;font-weight:700;color:#fff;width:600px;background:none;height:auto">We are engineering consultants and contractors</h1>
<p class="abs hero-sub">(EPC) in the oil and gas industry and building services industry.</p>
<div class="abs btn-orange slant" style="left:88px;top:556px;width:176px;height:48px">CONTACT US</div>
<div class="abs arrow slant" style="left:990px;top:645px"><svg width="10" height="12"><path d="M8 1 3 6l5 5" fill="none" stroke="#222" stroke-width="2"/></svg></div>
<div class="abs arrow slant" style="left:1050px;top:645px"><svg width="10" height="12"><path d="M2 1l5 5-5 5" fill="none" stroke="#222" stroke-width="2"/></svg></div>

<!-- who we are -->
<div class="abs who-frame"></div>
<div class="abs who-photo" role="img" aria-label="Photo of a red pipeline valve wheel against blue sky"></div>
<h2 class="abs title" style="left:585px;top:1012px">Who We Are</h2>
<p class="abs who-text">Veltranor undertakes Design, Supply, Installation and Commissioning of LPG and Petroleum systems including LPG Reticulated Systems (piped gas). We also do LPG tank revalidation and recertification.Our clients include: Oil companies (both multinationals and local), government agencies, manufacturing companies, agricultural institutions, and the building services industry.</p>
<div class="abs btn-outline" style="left:588px;top:1262px;width:176px;height:48px">READ MORE</div>

<!-- what we do -->
<h2 class="abs title" style="left:0;width:1200px;text-align:center;top:1440px">What we do</h2>
<div class="abs card" style="left:90px">
  <div class="card-img" role="img" aria-label="Photo of construction worker on site" style="background:linear-gradient(180deg,#9fb9cf,#c9b89a 60%,#8d7b62)"></div>
  <div class="card-icon"></div><div class="card-label">Engineering, procurement, construction</div>
</div>
<div class="abs card" style="left:349px">
  <div class="card-img" role="img" aria-label="Photo of engineer among process equipment" style="background:linear-gradient(180deg,#7d8288,#b2b3b0 55%,#6a6b6a)"></div>
  <div class="card-icon"></div><div class="card-label">Automation (safety and rocess)</div>
</div>
<div class="abs card" style="left:608px">
  <div class="card-img" role="img" aria-label="Photo of technician in orange coveralls testing pipework" style="background:linear-gradient(180deg,#7a6a56,#d07a3a 50%,#5b5048)"></div>
  <div class="card-icon"></div><div class="card-label">Non-destructive testing</div>
</div>
<div class="abs card" style="left:866px">
  <div class="card-img" role="img" aria-label="Photo of workers in safety vests at a training session" style="background:linear-gradient(180deg,#9a9a98,#d68450 55%,#6d6a66)"></div>
  <div class="card-icon"></div><div class="card-label" style="top:232px">Training</div>
</div>

<!-- projects -->
<h2 class="abs title" style="left:0;width:1200px;text-align:center;top:1892px">Our Projects</h2>
<div class="abs proj" style="left:0" role="img" aria-label="Photo of white LPG storage tank with dispensers" style=""></div>
<div class="abs proj" style="left:0;background:linear-gradient(180deg,#b9c6d2,#e8eaec 45%,#a9a8a4)" role="img" aria-label="Photo of white LPG storage tank with dispensers"></div>
<div class="abs proj" style="left:400px;background:linear-gradient(180deg,#5a5f63,#8b8e90)" role="img" aria-label="Photo of industrial steel structure"></div>
<div class="abs proj" style="left:800px;background:linear-gradient(180deg,#6f9fd0,#a8c6e4 50%,#6d6a68)" role="img" aria-label="Photo of red pipeline valve"></div>
<div class="abs proj-overlay"></div>
<div class="abs round-btn" style="left:558px;top:2196px"><svg width="16" height="16"><circle cx="7" cy="7" r="5" fill="none" stroke="#222" stroke-width="2"/><path d="M11 11l4 4" stroke="#222" stroke-width="2"/></svg></div>
<div class="abs round-btn" style="left:606px;top:2196px"><svg width="16" height="16"><path d="M6 10l4-4M5 8 3 10a2.5 2.5 0 0 0 3.5 3.5L8.5 11.5M11 8l2-2A2.5 2.5 0 0 0 9.5 2.5L7.5 4.5" fill="none" stroke="#222" stroke-width="1.8"/></svg></div>
<div class="abs round-btn" style="left:34px;top:2198px"><svg width="10" height="12"><path d="M8 1 3 6l5 5" fill="none" stroke="#222" stroke-width="2"/></svg></div>
<div class="abs round-btn" style="left:1116px;top:2198px"><svg width="10" height="12"><path d="M2 1l5 5-5 5" fill="none" stroke="#222" stroke-width="2"/></svg></div>

<!-- review -->
<h2 class="abs title" style="left:128px;top:2618px">Customer Review</h2>
<p class="abs review-text">Lorem Ipsum is simply dummy text of the printing and typesetting industry. Lorem Ipsum has been the industry's standard dummy text ever since the 1500s, when an unknown printer took a galley of type and scrambled it to make a type specimen book. It has survived not only five centuries, but also the leap into</p>
<div class="abs review-name">DANA MERCER</div>
<div class="abs round-btn" style="left:128px;top:2860px;width:64px;height:50px;background:#333"><svg width="10" height="12"><path d="M8 1 3 6l5 5" fill="none" stroke="#fff" stroke-width="2"/></svg></div>
<div class="abs round-btn" style="left:186px;top:2860px;width:64px;height:50px;background:var(--orange-light)"><svg width="10" height="12"><path d="M2 1l5 5-5 5" fill="none" stroke="#fff" stroke-width="2"/></svg></div>
<div class="abs collage"></div>
<div class="abs tile" style="left:712px;top:2618px;width:70px;height:64px;background:#c9c9c9" role="img" aria-label="Customer portrait"></div>
<div class="abs tile" style="left:908px;top:2610px;width:66px;height:56px;background:#d9a07a" role="img" aria-label="Customer portrait"></div>
<div class="abs tile" style="left:990px;top:2690px;width:74px;height:56px;background:#d8b25a" role="img" aria-label="Customer portrait"></div>
<div class="abs tile" style="left:782px;top:2718px;width:140px;height:96px;background:#ef5a6d" role="img" aria-label="Customer portrait"></div>
<div class="abs tile" style="left:816px;top:2830px;width:76px;height:56px;background:#bdbdbd" role="img" aria-label="Customer portrait"></div>
<div class="abs tile" style="left:632px;top:2862px;width:140px;height:96px;background:#3bbfc0" role="img" aria-label="Customer portrait"></div>
<div class="abs tile" style="left:928px;top:2852px;width:122px;height:96px;background:#c88a60" role="img" aria-label="Customer portrait"></div>

<!-- partners -->
<div class="abs partners">
  <span class="partner"><i></i>Ravelle</span>
  <span class="partner"><i></i>Pantero</span>
  <span class="partner"><i></i>Sorvik</span>
  <span class="partner"><i></i>Halden</span>
  <span class="partner"><i></i>Harlow Petroleum</span>
  <span class="partner"><i></i>Nordane Oil</span>
</div>

<!-- footer -->
<footer class="abs footer"></footer>
<div class="abs cta"></div>
<svg class="abs" style="left:265px;top:3347px" width="80" height="80" viewBox="0 0 80 80"><circle cx="40" cy="40" r="36" fill="none" stroke="#fff" stroke-width="3"/></svg>
<h2 class="abs cta h2" style="left:370px;top:3350px;font-size:38px;line-height:42px;color:#fff;font-weight:700;background:none;width:420px;height:auto;clip-path:none">Your Renovation Starts Here</h2>
<div class="abs slant" style="left:760px;top:3362px;width:176px;height:46px;background:#fff;color:#1f1f1f;font-size:13px;font-weight:700;display:flex;align-items:center;justify-content:center">FREE ESTIMATE</div>

<div class="abs brand" style="top:3594px;left:85px"><span class="brand-mark" style="width:80px;height:80px"></span><span class="brand-name" style="color:#bbb">VELTRANOR<br>LIMITED</span></div>
<p class="abs foot-col" style="left:86px;top:3686px;width:240px">Veltranor's core business is engineering works (Oil and Gas Engineering).</p>
<div class="abs foot-col" style="left:357px;width:240px">
  <b>Head Office:</b>Orchid Court, Next to Meridian Plaza, Kilima, Suite 14<br><br>Harbour Road<br>P.O. Box 40210-00500 Nairobi<br>
  <span class="ico">&#9742;</span>+254 700 555 010, +254 700 555 020<br><span class="ico">&#9993;</span>info@veltranor.example
</div>
<div class="abs foot-col" style="left:622px;width:240px">
  <b>Shop:</b>Coral Bank Building, Lakeview road Industrial Area<br>P.O. Box 40210-00500 Nairobi<br>
  <span class="ico">&#9742;</span>+254 700 555 010, +254 700 555 020<br><span class="ico">&#9993;</span>shop@veltranor.example
</div>
<div class="abs foot-col" style="left:884px;top:3590px;width:250px">
  <b>Rwanda Office</b>Veltranor Rwanda<br>Plot number 2204, Remera, Hillside, Kigali<br>
  <b style="margin-top:8px">Contact details:</b><span class="ico">&#9742;</span>+254 700 555 010, +254 700 555 020<br><span class="ico">&#9993;</span>rwanda@veltranor.example
</div>
<div class="abs" style="left:88px;top:3843px;width:1024px;height:1px;background:#444"></div>
<div class="abs slant" style="left:1117px;top:3807px;width:50px;height:40px;background:var(--orange-light);display:flex;align-items:center;justify-content:center"><svg width="12" height="8"><path d="M1 7l5-5 5 5" fill="none" stroke="#fff" stroke-width="2"/></svg></div>
<p class="abs copy">Copyright © 2023 VELTRANOR.All rights reserved.</p>

</body>
</html>
```